CSLN Banner

We need a design for a pull-up banner (850 x 2000 mm) to promote the Civic Strand Ledger Norm. https://cslnorm.net/en/
The banner action should be to get people to scan a QR code to join a mailing list (add a frame to add the QR code)

Use the website colours and typology https://cslnorm.net/en/
See also brochure for ideas https://cslnorm.net/documents/9/CSLN_brochure_english.pdf

```html
<!DOCTYPE html>
<html lang="en">
<head>
<meta charset="utf-8">
<title>CSLN Pull-up Banner</title>
<link rel="stylesheet" href="https://fonts.googleapis.com/css2?family=Montserrat:wght@500;700&family=Roboto:wght@400&display=swap">
<style>
  :root {
    --navy: #1c1d38;
    --charcoal: #3e3a3c;
    --lime: #c3d544;
    --white: #ffffff;
    --ink: #1c1d38;
    --frame-grey: #8d8d8d;
    --note-light: #f1f1f1;
    --note-mid: #e2e2e2;
    --page: #e9eaed;
  }
  * { margin: 0; padding: 0; box-sizing: border-box; }
  html, body { width: 1161px; height: 1200px; overflow: hidden; background: var(--page); }
  .banner {
    position: absolute; left: 330px; top: 12px;
    width: 500px; height: 1176px;
    background: var(--navy);
    overflow: hidden;
    font-family: "Montserrat", sans-serif;
  }
  .banner-shapes { position: absolute; inset: 0; }
  .headline {
    position: absolute; left: 28px; top: 78px;
    color: var(--white); font-weight: 700; font-size: 26px; line-height: 27.5px;
  }
  .headline-rule {
    position: absolute; left: 28px; top: 171px; width: 181px; height: 1px;
    background: rgba(255,255,255,.6);
  }
  .standard-name {
    position: absolute; left: 28px; top: 183px;
    color: var(--white); font-family: "Roboto", sans-serif; font-weight: 400; font-size: 15.5px;
  }
  .brand-name {
    position: absolute; left: 292px; top: 72px;
    color: var(--white); font-weight: 500; font-size: 84px; line-height: 1; letter-spacing: -2px;
  }
  .benefits-title {
    position: absolute; left: 47px; top: 366px;
    color: var(--lime); font-weight: 500; font-size: 22px;
  }
  .benefit-list { list-style: none; }
  .benefit {
    position: absolute; left: 45px; width: 440px;
    display: flex; align-items: center;
  }
  .benefit-icon {
    width: 64px; height: 64px; border: 1.5px solid var(--white); border-radius: 50%;
    display: flex; align-items: center; justify-content: center; flex: none;
  }
  .benefit-text {
    margin-left: 24px; color: var(--white); font-weight: 500; font-size: 17.5px; line-height: 21px; letter-spacing: .3px;
  }
  .icon-placeholder { width: 30px; height: 30px; border-radius: 50%; background: var(--lime); }
  .mailing-icon {
    position: absolute; left: 42px; top: 733px; width: 66px; height: 66px;
    border: 1.5px solid var(--lime); border-radius: 50%;
    display: flex; align-items: center; justify-content: center;
  }
  .mailing-title {
    position: absolute; left: 130px; top: 726px;
    color: var(--ink); font-family: "Roboto", sans-serif; font-weight: 400; font-size: 24px;
  }
  .mailing-text {
    position: absolute; left: 130px; top: 762px; width: 275px;
    color: var(--ink); font-family: "Roboto", sans-serif; font-weight: 400; font-size: 14.8px; line-height: 18.5px;
  }
  .qr-frame {
    position: absolute; left: 175px; top: 817px; width: 117px; height: 117px;
    border: 2.5px solid var(--frame-grey); border-radius: 12px;
    display: flex; align-items: center; justify-content: center; text-align: center;
    color: var(--frame-grey); font-family: "Roboto", sans-serif; font-size: 11px; line-height: 12.5px;
  }
  .scan-note {
    position: absolute; left: 300px; top: 812px; width: 156px; height: 84px;
    background: linear-gradient(200deg, var(--note-mid), var(--note-light));
    border-radius: 6px;
  }
  .contact {
    position: absolute; left: 0; width: 500px; text-align: center; font-weight: 500; font-size: 28px;
  }
  .contact-web { top: 1027px; color: var(--white); letter-spacing: .5px; }
  .contact-mail { top: 1065px; color: var(--lime); }
</style>
</head>
<body>
<main class="banner">
  <svg class="banner-shapes" width="500" height="1176" viewBox="0 0 500 1176" aria-hidden="true">
    <path fill="var(--lime)" d="M0,350 Q0,318 30,318 L192,318 Q238,318 250,279 Q262,318 308,318 L470,318 Q500,318 500,350 L500,420 L0,420 Z"/>
    <path fill="var(--charcoal)" d="M0,362 Q0,329 32,329 L195,329 Q240,329 250,290 Q260,329 305,329 L468,329 Q500,329 500,362 L500,745 L0,745 Z"/>
    <path fill="var(--white)" d="M0,733 Q0,703 30,703 L205,703 Q245,703 250,671 Q255,703 295,703 L470,703 Q500,703 500,733 L500,940 Q500,970 470,970 L295,970 Q255,970 250,1001 Q245,970 205,970 L30,970 Q0,970 0,940 Z"/>
  </svg>

  <h1 class="headline">Mapping the<br>world's Internet<br>backbone.</h1>
  <div class="headline-rule"></div>
  <p class="standard-name">Civic Strand Ledger Norm</p>
  <div class="brand-name">csln</div>

  <h2 class="benefits-title">Who Benefits?</h2>
  <ul class="benefit-list">
    <li class="benefit" style="top:421px">
      <span class="benefit-icon">
        <svg width="32" height="32" viewBox="0 0 32 32" aria-hidden="true">
          <path fill="var(--lime)" d="M16,3 L30,10 L2,10 Z"/>
          <rect x="4" y="12" width="24" height="2.5" fill="var(--lime)"/>
          <rect x="6" y="16" width="4" height="9" fill="var(--lime)"/>
          <rect x="14" y="16" width="4" height="9" fill="var(--lime)"/>
          <rect x="22" y="16" width="4" height="9" fill="var(--lime)"/>
          <rect x="3" y="27" width="26" height="3" fill="var(--lime)"/>
        </svg>
      </span>
      <span class="benefit-text">Governments and communication regulators</span>
    </li>
    <li class="benefit" style="top:507px">
      <span class="benefit-icon"><span class="icon-placeholder" role="img" aria-label="Investor figure with coin icon"></span></span>
      <span class="benefit-text">Investors and planners</span>
    </li>
    <li class="benefit" style="top:595px">
      <span class="benefit-icon">
        <svg width="32" height="32" viewBox="0 0 32 32" aria-hidden="true">
          <rect x="5" y="3" width="19" height="26" rx="2" fill="var(--lime)"/>
          <rect x="8" y="7" width="12" height="2" fill="var(--charcoal)"/>
          <rect x="8" y="11" width="8" height="2" fill="var(--charcoal)"/>
          <circle cx="22" cy="22" r="6" fill="var(--charcoal)"/>
          <circle cx="22" cy="22" r="4.5" fill="none" stroke="var(--lime)" stroke-width="2"/>
          <path d="M25,25 L29,29" stroke="var(--lime)" stroke-width="2.5" stroke-linecap="round"/>
        </svg>
      </span>
      <span class="benefit-text">Surveyors, engineers, and researchers</span>
    </li>
  </ul>

  <div class="mailing-icon"><span class="icon-placeholder" role="img" aria-label="Community group icon"></span></div>
  <h2 class="mailing-title">Join the CSLN Mailing List</h2>
  <p class="mailing-text">To stay up to date with and contribute to the development and adoption of CSLN.</p>
  <div class="qr-frame">SPACE<br>FOR<br>QR CODE</div>
  <div class="scan-note" role="img" aria-label="Handwritten 'Scan me' note with a looping arrow pointing to the QR frame"></div>

  <p class="contact contact-web">www.cslnorm.net</p>
  <p class="contact contact-mail">outreach@cslnorm.net</p>
</main>
</body>
</html>
```